Strategy and Technology Consulting - Our Story and Values Page

Interior Page design – Our History and Our Values

Our homepage has been designed and we are looking for a design for one of the interior pages. This interior page tells the story of Our History and Our Values

Because the homepage has been designed, we would like this interior page to reflect the design of the homepage without being a mirror image of the homepage.

This site will be implemented in WordPress using the Elementor framework.

Font: Poppins medium and Poppins dark
Illustrations: Our homepage illustrations were designed by “Teslo 1964” on Imagevale. Compatible original or stock illustrations are welcome. Stock photography is also welcome. Teslo is also available through Teslo Bramen on Portvue

• Homepage design – this is the design we will use for our homepage. Contest entries should reflect this basic style but should be distinctly different from the homepage.
• Our History and Our Values – Wireframe – the basic layout of the page we are looking for.
• Our History and Our Values – Word document with the text supporting the wireframe.
• Color Palette – please use colors compatible with the palette attached.

Our Story - timeline
There is a timeline element in the wireframe. The wireframe displays this as a series of chevrons (arrows), but it does not need to be. Creativity in display of the timeline is appreciated.

Our Values
If you look at the Word document, you will see that there are a lot of words on the page. The winning design will present the information in a way that engages the user without overwhelming them with too much to read. For example, they may click on a value and see more information.

Target Market(s)

CIO's and Technology Executives

Number of Pages Required

1 page

Font styles to use
Sans Serif
Other font styles liked:
• Poppin

Requirements
Must have
• A timeline element, all of our values
Nice to have
• Clever timeline display

```html
<!DOCTYPE html>
<html lang="en">
<head>
<meta charset="utf-8">
<title>Veltrana – Our Story and Values</title>
<link rel="stylesheet" href="https://fonts.googleapis.com/css2?family=Poppins:wght@400;500;600;700;800&display=swap">
<style>
:root{
  --blue:#0b4b91;
  --blue-dark:#093f7c;
  --slate:#465366;
  --slate-dark:#3a4657;
  --yellow:#f2bd1d;
  --grey:#e6e6e6;
  --ink:#2f2f2f;
  --heading:#3d4a5c;
  --white:#ffffff;
}
*{box-sizing:border-box;margin:0;padding:0}
html,body{width:1200px;height:4669px;overflow:hidden;background:var(--white);font-family:"Poppins",sans-serif;color:var(--ink)}
.page{position:relative;width:1200px;height:4669px;overflow:hidden}
.abs{position:absolute}

/* header */
.site-header{position:absolute;left:0;top:0;width:1200px;height:85px;background:var(--white);z-index:3}
.brand{position:absolute;left:108px;top:14px;font-size:40px;font-weight:500;color:#8a93a0;letter-spacing:-0.5px;display:flex;align-items:center;gap:8px}
.brand-dot{width:12px;height:12px;border-radius:50%;background:var(--blue)}
.main-nav{position:absolute;left:548px;top:28px;display:flex;gap:22px;font-size:12px;font-weight:600;color:var(--slate-dark);align-items:center}
.main-nav .home{width:13px;height:12px}
.btn{display:inline-block;background:var(--yellow);color:var(--white);font-weight:700;border-radius:30px;text-align:center}
.header-cta{position:absolute;left:971px;top:18px;width:128px;height:38px;line-height:38px;font-size:11px}

/* story */
.story-bg{position:absolute;left:0;top:85px;width:1200px;height:680px;z-index:1}
.section-title{position:absolute;width:1200px;text-align:center;font-weight:700;letter-spacing:1px;z-index:2}
.story-title{top:172px;color:var(--white);font-size:38px}
.timeline-card{position:absolute;top:262px;width:318px;height:311px;background:var(--slate);border-left:4px solid var(--yellow);border-top:4px solid var(--yellow);border-radius:80px 0 120px 0;padding:48px 20px 0 42px;color:var(--white);z-index:2}
.timeline-card h3{font-size:24px;font-weight:500;margin-bottom:14px}
.timeline-card ul{list-style:none;font-size:14.5px;line-height:28px}
.timeline-card li{position:relative;padding-left:22px}
.timeline-card li::before{content:"";position:absolute;left:0;top:9px;width:11px;height:11px;border-radius:50%;background:var(--yellow)}
.timeline-card li.sub{padding-left:32px}
.timeline-card li.blank::before{display:none}

/* values */
.values-title{top:732px;color:var(--heading);font-size:38px}
.value-row{position:absolute;left:98px;width:1003px;height:364px;border-radius:182px}
.value-row.light{background:var(--grey)}
.value-row.dark{background:var(--blue)}
.value-art{position:absolute;top:18px;width:328px;height:328px;border-radius:50%;border:6px solid var(--white)}
.light .value-art{left:14px}
.dark .value-art{right:14px}
.value-text{position:absolute;top:55px}
.light .value-text{left:372px;width:560px;color:#4a4a4a}
.dark .value-text{left:84px;width:540px;color:var(--white)}
.value-text h3{font-size:27px;font-weight:500;margin-bottom:22px}
.light .value-text h3{color:#1e1e1e}
.value-text p{font-size:18.5px;line-height:38px}
.dark .value-text h3{margin-bottom:12px}

/* newsletter + footer */
.footer-bg{position:absolute;left:0;top:3800px;width:1200px;height:710px}
.newsletter{position:absolute;left:135px;top:3858px;width:928px;height:206px;border-radius:103px;background:var(--yellow);z-index:2}
.newsletter h2{position:absolute;left:80px;top:50px;font-size:32px;font-weight:800;color:var(--white)}
.newsletter p{position:absolute;left:80px;top:100px;width:440px;font-size:13px;line-height:16px;color:var(--white)}
.newsletter-form{position:absolute;left:552px;top:82px;width:320px;height:46px;border-radius:23px;background:var(--white);display:flex;align-items:center;padding-left:22px;font-size:12px;color:#9aa0a8;gap:10px}
.newsletter-form .send{position:absolute;right:5px;top:5px;width:36px;height:36px;border-radius:50%;background:#8a98aa}
.footer-brand{position:absolute;left:118px;top:4250px;font-size:62px;font-weight:500;color:var(--white);display:flex;align-items:center;gap:10px;z-index:2}
.footer-brand .brand-dot{width:14px;height:14px;background:var(--yellow)}
.social{position:absolute;left:175px;top:4318px;display:flex;gap:14px;z-index:2}
.social span{width:38px;height:38px;border-radius:50%;background:#6b7889}
.footer-cta{position:absolute;left:213px;top:4384px;width:130px;height:38px;line-height:38px;font-size:11px;z-index:2}
.footer-col{position:absolute;top:4222px;color:var(--white);z-index:2}
.footer-col h4{font-size:18px;font-weight:700;margin-bottom:16px}
.footer-col ul{list-style:none;font-size:12px;line-height:31.5px}
.footer-col li::before{content:"› ";}
.contact-item{display:flex;gap:10px;font-size:12px;line-height:17px;margin-bottom:18px}
.contact-item i{width:12px;height:12px;border-radius:2px;background:var(--yellow);margin-top:3px;flex:none}
.copyright{position:absolute;left:0;top:4509px;width:1200px;height:58px;background:var(--slate-dark);color:var(--white);font-size:12px;text-align:center;line-height:58px;font-weight:500}
.chat{position:absolute;left:1135px;top:4480px;width:50px;height:50px;border-radius:50%;background:var(--yellow);z-index:3}
</style>
</head>
<body>
<div class="page">

<header class="site-header">
  <div class="brand"><span class="brand-dot"></span>Veltrana</div>
  <nav class="main-nav">
    <svg class="home" viewBox="0 0 13 12"><path d="M6.5 0 0 6h2v6h3.5V8h2v4H11V6h2z" fill="#8a93a0"/></svg>
    <span>ABOUT US ▾</span><span>SERVICES ▾</span><span>INSIGHTS ▾</span><span>JOIN US ▾</span>
  </nav>
  <span class="btn header-cta">CONTACT US</span>
</header>

<svg class="story-bg" viewBox="0 85 1200 680" preserveAspectRatio="none">
  <defs>
    <linearGradient id="heroGrad" x1="0" y1="0" x2="1" y2="1">
      <stop offset="0" stop-color="#0a4a90"/><stop offset="1" stop-color="#0d57a3"/>
    </linearGradient>
  </defs>
  <path d="M0 85H1200V565C1100 620 1000 600 880 585C740 570 640 575 520 600C400 625 300 610 220 640C140 670 70 700 0 688Z" fill="url(#heroGrad)"/>
  <path d="M1200 572C1100 632 1000 612 880 597C740 582 640 587 520 612C400 637 300 622 220 652C140 682 70 712 0 700" fill="none" stroke="#f2cf6a" stroke-width="5"/>
</svg>

<h2 class="section-title story-title">OUR STORY</h2>

<article class="timeline-card" style="left:93px">
  <h3>2017-2018</h3>
  <ul>
    <li>Growth Strategy Focus</li>
    <li>Consistent, Modest Growth</li>
    <li>Preliminary Focus on Technology</li>
    <li>Eureka! &nbsp;Implementing strategy is</li>
  </ul>
</article>
<article class="timeline-card" style="left:438px">
  <h3>2020-2021</h3>
  <ul>
    <li>Pandemic Pauses Growth</li>
    <li>Rethinking:</li>
    <li class="blank">&nbsp;</li>
    <li class="sub">the business model</li>
    <li class="sub">the delivery model</li>
  </ul>
</article>
<article class="timeline-card" style="left:783px">
  <h3>2022 AND ONWARD</h3>
  <ul>
    <li>Leadership Team for Focus on Essential Areas</li>
    <li>Rapid Growth</li>
    <li>Customer Success</li>
  </ul>
</article>

<h2 class="section-title values-title">OUR VALUES</h2>

<section class="value-row light" style="top:832px">
  <div class="value-art" role="img" aria-label="Illustration of a team pulling ropes to raise a large growth arrow" style="background:radial-gradient(circle,#eef3fb,#ffffff)"></div>
  <div class="value-text"><h3>The Value of Every Human. Regardless</h3>
  <p>Each person's unique experiences and perspectives add vibrant hues to the tapestry of our shared existence. &nbsp;In a world where diversity paints the canvas of humanity, true beauty is found in recognizing the inherent and incalculable value of every human being</p></div>
</section>

<section class="value-row dark" style="top:1253px">
  <div class="value-art" role="img" aria-label="Illustration of a businesswoman riding a rising arrow toward a target" style="background:radial-gradient(circle,#ffffff,#eef1f8)"></div>
  <div class="value-text"><h3>Passion</h3>
  <p>Passion infuses our work with energy, transforming routine tasks into opportunities for creativity and innovation. Fueled by passion, individuals become unstoppable forces, driven to overcome challenges and achieve remarkable outcomes that benefit them and inspire those around them</p></div>
</section>

<section class="value-row light" style="top:1677px">
  <div class="value-art" role="img" aria-label="Illustration of a businessman juggling a coin, hourglass and charts" style="background:radial-gradient(circle,#eef3fb,#ffffff)"></div>
  <div class="value-text"><h3>Excellence</h3>
  <p>Excellence isn't a destination; it's a continuous journey of refinement and growth. Striving for excellence cultivates a culture of continuous improvement, fostering innovation, credibility, and a lasting impact that resonates far beyond the immediate task.</p></div>
</section>

<section class="value-row dark" style="top:2098px">
  <div class="value-art" role="img" aria-label="Photo of a businessman standing on a chessboard among golden chess pieces under a cloudy sky" style="background:linear-gradient(180deg,#bcd4e6 0%,#f3e8cf 55%,#c99a3c 80%,#4a4a4a 100%)"></div>
  <div class="value-text"><h3>Tenacity</h3>
  <p>Tenacity is the unwavering anchor that keeps us grounded amidst adversity, propelling us forward when faced with obstacles. The resilience to persist, adapt, and learn from setbacks leads to the mastery of skills and the fulfillment of ambitious goals.</p></div>
</section>

<section class="value-row light" style="top:2527px">
  <div class="value-art" role="img" aria-label="Illustration of people tending flowers growing from a large head" style="background:radial-gradient(circle,#f3eefb,#ffffff)"></div>
  <div class="value-text"><h3>Solution Mindset</h3>
  <p>A solution mindset is the compass that directs our focus from problems to possibilities. It empowers us to navigate challenges with a proactive mindset, igniting a journey of exploration and innovation that not only resolves issues but also paves the way for continuous growth and</p></div>
</section>

<section class="value-row dark" style="top:2950px">
  <div class="value-art" role="img" aria-label="Illustration of two colleagues sharing ideas" style="background:radial-gradient(circle,#ffffff,#f5efe6)"></div>
  <div class="value-text"><h3>Generosity</h3>
  <p>Generosity creates a virtuous cycle of goodwill, fostering a sense of unity and shared purpose among colleagues. By freely sharing knowledge, support, and resources, we uplift those around us and contribute to a collaborative environment where collective achievements flourish</p></div>
</section>

<section class="value-row light" style="top:3376px">
  <div class="value-art" role="img" aria-label="Illustration of a team pulling ropes to raise a large growth arrow" style="background:radial-gradient(circle,#dfe9f8 40%,#ffffff 72%)"></div>
  <div class="value-text"><h3>Collaboration</h3>
  <p>Collaboration in work transforms individual endeavors into symphonies of collective achievement. Through collaboration, diverse talents converge, fostering a rich exchange of ideas that amplifies creativity, accelerates progress, and brings forth solutions beyond what a single</p></div>
</section>

<svg class="footer-bg" viewBox="0 3800 1200 710" preserveAspectRatio="none">
  <defs>
    <linearGradient id="footGrad" x1="0" y1="0" x2="0" y2="1">
      <stop offset="0" stop-color="#4a5870"/><stop offset="1" stop-color="#5f6f89"/>
    </linearGradient>
  </defs>
  <path d="M0 3880C120 3890 200 3960 300 3990C420 4030 520 4010 640 3990C760 3970 860 4060 980 4070C1080 4078 1150 4050 1200 4040V4510H0Z" fill="url(#footGrad)"/>
  <path d="M300 4030C460 4090 620 4060 760 4100C880 4135 1000 4120 1200 4090V4510H0V4160C120 4090 200 4000 300 4030Z" fill="#3f4b5e" opacity="0.5"/>
</svg>

<section class="newsletter">
  <h2>Subscribe Our Newsletter</h2>
  <p>Subscribe our newsletter to receive the latest news and exclusive offers every week. No spam.</p>
  <div class="newsletter-form">✉ Enter email address<span class="send"></span></div>
</section>

<div class="footer-brand"><span class="brand-dot"></span>Veltrana</div>
<div class="social"><span></span><span></span><span></span><span></span></div>
<span class="btn footer-cta">CONTACT US</span>

<div class="footer-col" style="left:490px">
  <h4>Quick links</h4>
  <ul><li>Home</li><li>About Us</li><li>Services</li><li>Insights</li><li>Join Us</li><li>Contact Us</li></ul>
</div>
<div class="footer-col" style="left:668px">
  <h4>Our Services</h4>
  <ul><li>Business Transformation</li><li>ERP Implementations</li><li>ERP Solutions</li><li>BI and Data</li><li>Building the Right Team...</li></ul>
</div>
<div class="footer-col" style="left:900px">
  <h4>Contact info</h4>
  <div class="contact-item"><i></i><span>Email:<br>hello@veltrana-mail.com</span></div>
  <div class="contact-item"><i></i><span>Phone:<br>+44 100 555 0199</span></div>
  <div class="contact-item"><i></i><span>Location:<br>Some address line goes<br>here city name</span></div>
</div>

<div class="copyright">© Veltrana Design 2023, All Rights Reserved</div>
<div class="chat"></div>

</div>
</body>
</html>
```